Brill Insurance Agency - Business Cards

Hello, I am needing new trendy business cards for our Insurance Agency now that I have a new Logo. I have attached our new logo with several color options along with a business card design that I like. I am leaning towards burgundy and blue colors. I have attached our current business card. I have also attached a headshot of our company president, Martin Vale, that you can use if you wish. Thank you so much in advance for all the wonderful designs!!!!

Target Market(s)

We want to look very professional to potential customers and we also want to look very professional so insurance companies will want to contract with us to sell their product.

Industry/Entity Type

Insurance

Contact Information for Business Card

Martin Vale
mvale@brillagency.com
Business: 555-213-4087
Fax: 555-213-7751
Cell: 555-390-2618
Toll Free: 888-555-0194
42 W Elm Rd Butler, MO 64730
www.brillagency.net

Font styles to use
Serif
Sans Serif

Colors
0355a3
3277b5
f04a50
ec1f27

Requirements
Nice to have
• I love creativity. The more creative and balanced a business card design the more I will like it. I would like the card to be printed horizontally instead of vertically.
Should not have
• My project should not have the Allied Coverage Network logo. It is no longer used in the industry.

```html
<!DOCTYPE html>
<html lang="en">
<head>
<meta charset="utf-8">
<title>Brill Insurance Agency – Business Cards</title>
<link rel="stylesheet" href="https://fonts.googleapis.com/css2?family=Montserrat:wght@700&family=Open+Sans:wght@400;700&display=swap">
<style>
  :root {
    --bg: #2a2a2c;
    --card-white: #ffffff;
    --burgundy: #5a0f24;
    --burgundy-deep: #4b0c1e;
    --slate: #444446;
    --ink-grey: #5b5b5d;
    --ring-grey: #6a6a6c;
    --text-light: #f2f2f2;
  }
  * { box-sizing: border-box; margin: 0; padding: 0; }
  html, body { width: 1200px; height: 1000px; overflow: hidden; }
  body {
    background: var(--bg);
    font-family: "Open Sans", Arial, sans-serif;
    position: relative;
  }
  .card {
    position: absolute;
    left: 300px;
    width: 600px;
    height: 343px;
    border-radius: 22px;
    background: var(--card-white);
    overflow: hidden;
    box-shadow: 0 14px 30px rgba(0,0,0,.45);
  }
  .card--back { top: 100px; }
  .card--front { top: 557px; }

  /* back */
  .back-brand {
    position: absolute;
    top: 112px; left: 0; right: 0;
    display: flex; align-items: center; justify-content: center; gap: 22px;
  }
  .brand-dot {
    width: 74px; height: 74px; border-radius: 50%;
    border: 7px solid var(--ring-grey);
    background: var(--card-white);
  }
  .brand-divider { width: 2px; height: 80px; background: var(--ink-grey); }
  .wordmark {
    font-family: "Montserrat", Arial, sans-serif;
    font-weight: 700;
    color: var(--burgundy);
    text-transform: uppercase;
    line-height: 1.05;
  }
  .back-brand .wordmark { font-size: 27px; letter-spacing: .5px; }
  .back-web {
    position: absolute; bottom: 52px; left: 0; right: 0;
    text-align: center;
    color: var(--ink-grey);
    font-size: 18px; letter-spacing: 4px;
  }

  /* front */
  .front-brand {
    position: absolute; top: 58px; left: 0; right: 0;
    text-align: center;
  }
  .front-brand .wordmark { font-size: 30px; letter-spacing: .5px; }
  .contact-band {
    position: absolute; left: 0; right: 0; bottom: 0; height: 170px;
    background: var(--slate);
  }
  .person-panel {
    position: absolute; left: 0; top: 0; bottom: 0; width: 280px;
    background: var(--burgundy-deep);
    color: var(--text-light);
    padding: 20px 0 0 28px;
  }
  .person-name { font-weight: 700; font-size: 22px; letter-spacing: .5px; }
  .person-title { font-size: 14px; text-transform: uppercase; margin-bottom: 4px; }
  .person-address { font-size: 14px; line-height: 1.3; }
  .band-dot {
    position: absolute; left: 218px; top: -24px;
    width: 124px; height: 124px; border-radius: 50%;
    background: var(--card-white);
    border: 6px solid var(--ring-grey);
  }
  .contact-list {
    position: absolute; right: 22px; top: 58px;
    list-style: none;
    color: var(--text-light);
    font-size: 17px; line-height: 1.5;
  }
  .contact-list li { display: flex; align-items: center; justify-content: flex-end; gap: 12px; }
  .contact-list svg { width: 16px; height: 16px; fill: #d9d9d9; flex: none; }
</style>
</head>
<body>
  <section class="card card--back" aria-label="Business card back">
    <div class="back-brand">
      <span class="brand-dot"></span>
      <span class="brand-divider"></span>
      <div class="wordmark">Brill Insurance<br>Agency Inc</div>
    </div>
    <p class="back-web">brillagency.net</p>
  </section>

  <section class="card card--front" aria-label="Business card front">
    <div class="front-brand">
      <div class="wordmark">Brill Insurance<br>Agency Inc</div>
    </div>
    <div class="contact-band">
      <div class="person-panel">
        <p class="person-name">MARTIN VALE</p>
        <p class="person-title">President</p>
        <p class="person-address">42 W Elm Rd P.O.Box 318<br>Harlow, MO 64912</p>
      </div>
      <span class="band-dot"></span>
      <ul class="contact-list">
        <li>555-213-4087,ext.23
          <svg viewBox="0 0 16 16" aria-hidden="true"><path d="M2 5c0-2 3-3 6-3s6 1 6 3v1h-3V5H5v1H2zM4 8h8l2 6H2z"/></svg></li>
        <li>888-555-0194 (TF)
          <svg viewBox="0 0 16 16" aria-hidden="true"><path d="M4 1h8v14H4zM5 3v9h6V3z"/></svg></li>
        <li>555-213-7751
          <svg viewBox="0 0 16 16" aria-hidden="true"><path d="M4 1h8v5H4zM2 7h12v8H2zM4 10v2h8v-2z"/></svg></li>
        <li>mvale@brillagency.net
          <svg viewBox="0 0 16 16" aria-hidden="true"><path d="M1 3h14v10H1zM2 4l6 5 6-5z"/></svg></li>
      </ul>
    </div>
  </section>
</body>
</html>
```